I am a company selling interior designing materials

HI, I am selling interior design materials and require a namecard which is more outstanding while following a certain details placement as attached.

My clients are mainly interior designers so it has to attract their attention rather than feeling that its "just another namecard". I am selling wallcoverings, fabrics, acoustics and carpets.

Target Market(s)

interior designers designing hotels, commerical offices.

Contact Information for Business Card

As per attached.
Please change address to 47 Jalan 16 Tampines #05-11 Vexor Tower Singapore 529341

Font styles to use
Other font styles liked:
• calibri

Requirements
Must have
• (1) company logo on top in the middle. Placement of contac details to be the same
• (2) company color is blue/green cymk 75/8/42/0
• (3) "KTV" logo to be prominent
• (4) You may change the logo but there should be a "swirl" surrounding the word KTV like current logo. The swirl pattern does not need to follow current logo and you may propose.
Should not have
• (1) there should not be any designs above "KTV" logo
• (2) no sharp triangles or angles

```html
<!DOCTYPE html>
<html lang="en">
<head>
<meta charset="utf-8">
<title>KTV Business Card</title>
<link href="https://fonts.googleapis.com/css2?family=Arimo:wght@400;700&family=Carlito:wght@400;700&display=swap" rel="stylesheet">
<style>
  :root {
    --backdrop: #2b2b2b;
    --card-white: #f3f3f3;
    --brand-teal: #1fa89c;
    --ink-grey: #555555;
    --ink-white: #ffffff;
  }
  * { margin: 0; padding: 0; box-sizing: border-box; }
  html, body {
    width: 1200px;
    height: 960px;
    overflow: hidden;
    background: var(--backdrop);
  }
  .canvas {
    position: relative;
    width: 1200px;
    height: 960px;
  }
  .card {
    position: absolute;
    width: 600px;
    height: 342px;
    border-radius: 22px;
  }
  .card-front {
    left: 302px;
    top: 124px;
    background: var(--card-white);
  }
  .card-back {
    left: 299px;
    top: 493px;
    background: var(--brand-teal);
  }
  .brand-mark {
    position: absolute;
    left: 100px;
    top: 52px;
    width: 165px;
    text-align: center;
    font-family: "Carlito", "Calibri", sans-serif;
    font-weight: 700;
    font-size: 42px;
    letter-spacing: 1px;
    color: var(--ink-grey);
    line-height: 1;
  }
  .company-name {
    position: absolute;
    left: 52px;
    top: 124px;
    font-family: "Carlito", "Calibri", sans-serif;
    font-weight: 700;
    font-size: 14px;
    color: var(--ink-grey);
  }
  .person-name {
    position: absolute;
    left: 52px;
    top: 239px;
    font-family: "Arimo", sans-serif;
    font-weight: 700;
    font-size: 21px;
    color: var(--brand-teal);
    transform: scaleX(0.92);
    transform-origin: left;
  }
  .address {
    position: absolute;
    left: 336px;
    top: 200px;
    font-family: "Arimo", sans-serif;
    font-size: 14px;
    line-height: 18px;
    color: var(--ink-grey);
  }
  .contact-list {
    position: absolute;
    left: 336px;
    top: 246px;
    list-style: none;
    font-family: "Arimo", sans-serif;
    font-size: 14px;
    line-height: 19px;
    color: var(--ink-grey);
  }
  .contact-list li {
    display: flex;
    align-items: center;
    gap: 8px;
  }
  .contact-list svg {
    width: 13px;
    height: 13px;
    fill: var(--brand-teal);
    flex: none;
  }
  .brand-mark-large {
    position: absolute;
    left: 0;
    top: 140px;
    width: 100%;
    text-align: center;
    font-family: "Carlito", "Calibri", sans-serif;
    font-weight: 700;
    font-size: 60px;
    letter-spacing: 2px;
    color: var(--ink-white);
    line-height: 1;
  }
  .product-line {
    position: absolute;
    left: 0;
    top: 300px;
    width: 100%;
    text-align: center;
    font-family: "Arimo", sans-serif;
    font-size: 14px;
    color: var(--ink-white);
  }
</style>
</head>
<body>
<main class="canvas">
  <section class="card card-front">
    <div class="brand-mark">KTV</div>
    <div class="company-name">KenTaVio Interior Furnishings Pte Ltd</div>
    <div class="person-name">JOANNE LIM</div>
    <address class="address" style="font-style:normal">
      47 Jalan 16 Tampines #05-11<br>
      Vexor Tower Singapore 529341
    </address>
    <ul class="contact-list">
      <li>
        <svg viewBox="0 0 13 13" aria-hidden="true"><path d="M3.5 0h6a1 1 0 0 1 1 1v11a1 1 0 0 1-1 1h-6a1 1 0 0 1-1-1V1a1 1 0 0 1 1-1zm.5 1.5v8.5h5V1.5zM6.5 10.8a.8.8 0 1 0 0 1.6.8.8 0 0 0 0-1.6z"/></svg>
        (65) 9172 4630
      </li>
      <li>
        <svg viewBox="0 0 13 13" aria-hidden="true"><path d="M1 3h11v7H1zM1.6 3.4 6.5 7l4.9-3.6v1L6.5 8 1.6 4.4z" fill-rule="evenodd"/></svg>
        joanne@ktvfurnishing.com
      </li>
      <li>
        <svg viewBox="0 0 13 13" aria-hidden="true"><circle cx="6.5" cy="6.5" r="6"/><path d="M4 4.5c1 0 1.5.8 2.5.5s.5 1.5-.5 2-.5 2-1.5 2.5C4 8 3.5 6 4 4.5zM8.5 3c1 .5 2 1.5 2 3-1 0-1.5-1-2.5-1z" fill="#f3f3f3"/></svg>
        www.ktvfurnishing.com
      </li>
    </ul>
  </section>
  <section class="card card-back">
    <div class="brand-mark-large">KTV</div>
    <p class="product-line">Wallcoverings &nbsp;•&nbsp; Acoustic &nbsp;•&nbsp; Fabrics &nbsp;•&nbsp; Carpet</p>
  </section>
</main>
</body>
</html>
```